The Maplewood Learning House Web Page

We need a web design for our Day Care Center based in Brandon, Florida. We are targeting child care and educational services to middle class parents, specially the mother. We would like to see designs that matches attached logo mark. The final design should communicate higher standards for day care and educational services.

Middle class parents in the State of Florida

```html
<!DOCTYPE html>
<html lang="en">
<head>
<meta charset="utf-8">
<title>The Maplewood Learning House</title>
<link rel="stylesheet" href="https://fonts.googleapis.com/css2?family=Open+Sans:wght@300;400;600;700&display=swap">
<style>
:root{
  --navy:#03203f;
  --orange:#fbb436;
  --cta:#f26522;
  --cyan:#37d1fa;
  --green:#9bbd2c;
  --slate:#7f95a8;
  --white:#ffffff;
  --text:#1c1c1c;
}
*{box-sizing:border-box;margin:0;padding:0}
html,body{width:933px;height:1200px;overflow:hidden;background:var(--white);font-family:"Open Sans",sans-serif;color:var(--text)}
.page{position:relative;width:933px;height:1200px}
.sidebar{position:absolute;left:0;top:0;width:200px;height:1200px;background:var(--navy)}
.brand{position:absolute;left:16px;top:44px;width:168px;text-align:center;color:var(--orange);font-size:14px;font-weight:600;line-height:19px}
.brand-mark{display:block;width:14px;height:14px;border-radius:50%;background:var(--orange);margin:0 auto 8px}
.nav{position:absolute;left:0;top:170px;width:200px;list-style:none}
.nav li{position:relative;height:31.1px;line-height:31.1px;padding-left:34px;color:var(--white);font-size:12px}
.nav li.active{background:var(--orange)}
.nav .chev{position:absolute;right:24px;top:0;font-size:11px}
.submenu{position:absolute;left:206px;top:200px;width:170px;height:84px;background:var(--orange);padding:12px 0 0 16px;color:var(--white);font-size:12px;line-height:19.5px;z-index:3}
.copyright{position:absolute;left:35px;top:804px;width:165px;height:56px;background:var(--slate);color:var(--white);font-size:24px;line-height:56px;padding-left:18px}
.social{position:absolute;left:231px;top:26px;display:flex;gap:6px}
.social span{width:21px;height:21px;border-radius:50%}
.phone{position:absolute;right:36px;top:25px;font-size:12.5px;color:var(--navy);display:flex;align-items:center;gap:10px}
.hero{position:absolute;left:229px;top:71px;width:704px;height:403px;background:linear-gradient(110deg,#e9d6c3 0%,#d7a98a 35%,#c98d6e 50%,#7fae6a 80%,#d9c9b6 100%)}
.dots{position:absolute;left:855px;top:95px;display:flex;gap:4px}
.dots span{width:11px;height:11px;border-radius:50%;background:var(--white)}
.dots span.on{background:var(--navy);border:3px solid var(--white)}
.welcome{position:absolute;left:502px;top:303px;width:431px;height:111px;background:rgba(255,255,255,.88);padding:20px 0 0 27px}
.welcome h1{font-weight:400;font-size:18.5px;color:#111;line-height:26px;white-space:nowrap}
.welcome p{font-size:12.5px;line-height:16px;margin-top:4px;color:#222;width:395px}
.btn-apply{position:absolute;left:718px;top:399px;width:182px;height:34px;background:var(--cta);color:var(--white);font-size:13px;display:flex;align-items:center;justify-content:center;gap:6px}
.intro{position:absolute;left:229px;top:504px;width:680px;font-size:23px;font-weight:400;line-height:28px;color:var(--navy)}
.services{position:absolute;left:230px;top:582px;display:flex;gap:8px}
.service{width:164px;text-align:center}
.service .photo{height:112px}
.service h3{font-size:10.5px;font-weight:700;color:var(--navy);margin-top:11px}
.service p{font-size:10.5px;line-height:12.5px;margin-top:8px}
.panel{position:absolute;top:804px;height:326px;width:223px;color:var(--white);padding:0 20px}
.panel h2{font-weight:300;font-size:20px;margin-top:29px;line-height:26px}
.panel .photo{width:186px;height:112px;margin-top:14px}
.about{left:230px;background:var(--cyan)}
.admissions{left:458px;background:var(--green)}
.contact{left:686px;background:var(--orange);padding-left:23px}
.about p{font-size:10.5px;line-height:12.5px;margin-top:20px}
.more{position:absolute;left:20px;bottom:24px;font-size:13px}
.links{list-style:none;margin-top:18px;font-size:12px}
.links li{height:24.5px;display:flex;align-items:center;gap:5px}
.field{width:177px;height:29px;background:var(--white);color:#888;font-size:10.5px;padding:8px 9px;margin-top:4px}
.field.first{margin-top:16px}
.field.msg{height:81px}
.submit{width:105px;height:29px;background:var(--navy);color:var(--white);font-size:13px;text-align:center;line-height:29px;margin-top:14px}
</style>
</head>
<body>
<div class="page">
  <aside class="sidebar">
    <div class="brand"><span class="brand-mark"></span>The Maplewood<br>Learning House</div>
    <ul class="nav">
      <li>Home</li>
      <li class="active">Admissions<span class="chev">&gt;</span></li>
      <li>Philosophy<span class="chev">&gt;</span></li>
      <li>Programs<span class="chev">&gt;</span></li>
      <li>Services<span class="chev">&gt;</span></li>
      <li>Campuses<span class="chev">&gt;</span></li>
      <li>Franchises<span class="chev">&gt;</span></li>
      <li>Business</li>
      <li>Contact</li>
      <li>Preferred Vendors</li>
      <li>Real Estate</li>
      <li>Business Co-Ops</li>
      <li>Career Opportunities</li>
      <li>Privacy Policy</li>
      <li>Franchise Privacy Policy</li>
    </ul>
    <div class="copyright">© 2015</div>
  </aside>

  <div class="submenu">Apply for Admission<br>Schedule a Campus Tour<br>Enrollment Policy</div>

  <div class="social">
    <span style="background:#3ec6f4"></span>
    <span style="background:#f7b436"></span>
    <span style="background:#8dc63f"></span>
  </div>
  <div class="phone">
    <svg width="14" height="16" viewBox="0 0 24 24"><path fill="#03203f" d="M6.6 10.8a15.1 15.1 0 0 0 6.6 6.6l2.2-2.2c.3-.3.7-.4 1-.2 1.1.4 2.3.6 3.6.6.6 0 1 .4 1 1V20c0 .6-.4 1-1 1A17 17 0 0 1 3 4c0-.6.4-1 1-1h3.5c.6 0 1 .4 1 1 0 1.3.2 2.5.6 3.6.1.3 0 .7-.2 1z"/></svg>
    +1 555 0142 77
  </div>

  <div class="hero" role="img" aria-label="Smiling young girl with classmates painting at a classroom table"></div>
  <div class="dots"><span></span><span class="on"></span><span></span></div>
  <div class="welcome">
    <h1>Welcome to The Maplewood Learning House</h1>
    <p>Lorem ipsum dolor amet, consectetur adipisicing , tempor elit incididunt ut labore dolore magna aliqua eiusmod.. More</p>
  </div>
  <div class="btn-apply">Apply to Admission
    <svg width="13" height="13" viewBox="0 0 24 24"><path fill="#fff" d="M12 2l3 7h7l-5.6 4.4 2 7.6L12 16.8 5.6 21l2-7.6L2 9h7z"/></svg>
  </div>

  <h2 class="intro">We belive to deliver child care and educational services to middle class parents</h2>

  <div class="services">
    <div class="service"><div class="photo" role="img" aria-label="Caregiver holding a baby in a playroom" style="background:linear-gradient(135deg,#6b4a3a,#d9b89a)"></div><h3>Home School Support</h3><p>Lorem ipsum dolor consectetur adipisicing elit, sed do eiusmod tempor incididun</p></div>
    <div class="service"><div class="photo" role="img" aria-label="Teacher with children in a classroom" style="background:linear-gradient(135deg,#b86b4a,#e7c2a6)"></div><h3>School Readiness Provider</h3><p>Lorem ipsum dolor consectetur adipisicing elit, sed do eiusmod tempor incididun</p></div>
    <div class="service"><div class="photo" role="img" aria-label="Teacher helping children draw" style="background:linear-gradient(135deg,#e0603a,#f1d8c4)"></div><h3>Voluntary Pre-K (VPK)</h3><p>Lorem ipsum dolor consectetur adipisicing elit, sed do eiusmod tempor incididun</p></div>
    <div class="service"><div class="photo" role="img" aria-label="Children painting at a table" style="background:linear-gradient(135deg,#e8d3bf,#c88f6c 55%,#7fae6a)"></div><h3>Enrichment Services</h3><p>Lorem ipsum dolor consectetur adipisicing elit, sed do eiusmod tempor incididun</p></div>
  </div>

  <section class="panel about">
    <h2>About Us</h2>
    <div class="photo" role="img" aria-label="Caregiver holding a baby in a playroom" style="background:linear-gradient(135deg,#6b4a3a,#d9b89a)"></div>
    <p>Lorem ipsum dolor sit consectetur adipisicing elit, sed do incididunt ut labore dolore aliqua. Ut enim ad veniam, quis ullamco laboris nisi ut commodo consequat reprehenderit voluptate velit esse dolore</p>
    <div class="more">Learn More&gt;&gt;</div>
  </section>

  <section class="panel admissions">
    <h2>Admissions</h2>
    <div class="photo" role="img" aria-label="Children playing with colourful toys" style="background:linear-gradient(135deg,#d2463a,#e8c9a8 50%,#3a62b0)"></div>
    <ul class="links">
      <li><svg width="12" height="12" viewBox="0 0 24 24"><path fill="#fff" d="M12 2l3 7h7l-5.6 4.4 2 7.6L12 16.8 5.6 21l2-7.6L2 9h7z"/></svg>Apply for Admission</li>
      <li><svg width="12" height="12" viewBox="0 0 24 24"><path fill="#fff" d="M12 2l3 7h7l-5.6 4.4 2 7.6L12 16.8 5.6 21l2-7.6L2 9h7z"/></svg>Schedule a Campus Tour</li>
      <li><svg width="12" height="12" viewBox="0 0 24 24"><path fill="#fff" d="M12 2l3 7h7l-5.6 4.4 2 7.6L12 16.8 5.6 21l2-7.6L2 9h7z"/></svg>Enrollment Policy</li>
    </ul>
    <div class="more">Learn More&gt;&gt;</div>
  </section>

  <section class="panel contact">
    <h2>Get in Touch</h2>
    <div class="field first">User Name</div>
    <div class="field">Email ID</div>
    <div class="field">Phone</div>
    <div class="field msg">Message</div>
    <div class="submit">Submit</div>
  </section>
</div>
</body>
</html>
```